Webdesign  Seminare im Bereich persönliche Entwicklung, Spiritualität und Coaching
Webdesign Seminare im Bereich persönliche Entwicklung, Spiritualität und Coaching
Zielgruppe
Wir bieten Seminare im Bereich persönliche Entwicklung, Spiritualität und Coaching an. Unsere Zielgruppe umfasst Menschen zw. 18 und 75 jeglichen Berufsstandes, die sich dafür interessieren ihre tieferen innewohnenden Potenziale kennenzulernen und zu eröffnen.
Dieser Auftrag hier ist ein Teaser-Projekt. Wir wachsen konstant, möchten mehrere Folgeaufträge vergeben und suchen auf diesem Weg einen langfristigen Partner.
Aufgabenstellung
- keine esoterischen Klischee-Bilder, nichts Verspieltes
- unser Auftritt (hier vorerst die Website) soll wärmer wirken als dies aktuell der Fall ist, die Klarheit darf dabei jedoch nicht verloren gehen
- klar, warm, offen, vertraut, seriös
- das Logo darf verändert werden
Aktuell ist recht wenig Bildmaterial vorhanden. Hier wird demnächst nachproduziert. Bitte vorerst, wenn designtechnisch angebracht, Stockmaterial (als Platzhalter) verwenden.

```html
<!DOCTYPE html>
<html lang="de">
<head>
<meta charset="utf-8">
<title>Lesen im ResonanzRaum – Julius Brandt</title>
<link href="https://fonts.googleapis.com/css2?family=Playfair+Display:ital,wght@0,400;0,600;0,700;1,400&family=Poppins:ital,wght@0,400;0,500;0,600;1,400&display=swap" rel="stylesheet">
<style>
:root{
  --blue:#45afd3;
  --cream:#fffdf6;
  --yellow:#ffd97a;
  --ink:#2b2b2b;
  --text:#3d3d3d;
  --rule:#cfe6ea;
  --white:#ffffff;
}
*{margin:0;padding:0;box-sizing:border-box}
html,body{width:1200px;height:3687px;overflow:hidden}
body{position:relative;background:var(--cream);font-family:'Poppins',sans-serif;color:var(--text)}
.abs{position:absolute}
.serif{font-family:'Playfair Display',serif}
.center{text-align:center}
.btn{position:absolute;background:var(--blue);color:var(--white);font-size:11px;font-weight:500;display:flex;align-items:center;justify-content:center;gap:6px;height:26px}
.btn svg{width:14px;height:10px}
.site-header{left:0;top:0;width:1200px;height:62px;background:var(--blue);z-index:3}
.brand{left:223px;top:20px;color:var(--white);font-family:'Poppins',sans-serif;font-weight:500;font-size:17px;line-height:22px}
.nav{right:223px;top:24px;display:flex;gap:31px;font-size:11px;font-weight:600;color:var(--white)}
.nav .active{border-bottom:1px solid var(--white);padding-bottom:3px}
.hero{left:0;top:0;width:1200px;height:540px;background:linear-gradient(180deg,#3aa6d4 0%,#4eb0d8 30%,#8ccbe0 55%,#cfe2d8 75%,#fbe8b0 92%,#ffe9a0 100%)}
.hero-curve{left:0;top:470px;width:1200px;height:80px}
.hero-title{left:0;width:1200px;color:var(--white);text-align:center;font-family:'Playfair Display',serif}
.tabs{top:588px;left:223px;width:754px;display:flex;font-family:'Playfair Display',serif;font-size:22px;font-weight:600;color:var(--ink)}
.tabs span{flex:1;text-align:center}
.tabs .on{color:var(--blue)}
.rule{height:1px;background:var(--rule)}
.short-rule{height:2px;width:86px;background:var(--rule);left:557px}
.para{font-size:11.5px;line-height:16px;text-align:center;color:var(--text)}
.ph{position:absolute;border-radius:6px}
.video{background:linear-gradient(90deg,#8b6c5c 0%,#c6b7a5 40%,#2a2a2a 70%,#1e1e1e 100%);width:238px;height:146px}
.play{position:absolute;left:107px;top:61px;width:24px;height:24px;border-radius:50%;background:var(--blue)}
.feat{width:220px;text-align:center;top:1688px}
.feat h3{font-size:16px;font-weight:500;color:var(--ink);line-height:20px;margin-bottom:18px}
.feat p{font-size:10.5px;line-height:15px}
.band{left:0;top:1880px;width:1200px;height:414px;background:var(--yellow)}
.card{position:absolute;background:var(--white);box-shadow:0 2px 6px rgba(0,0,0,.08);width:238px;text-align:center;border-radius:3px;overflow:hidden}
.card .img{height:153px}
.card h4{font-size:16px;font-weight:500;color:var(--ink);margin:14px 10px 10px;line-height:17px}
.card p{font-size:9px;line-height:13.5px;padding:0 22px}
.card .btn{right:20px;bottom:20px;width:90px}
.footer-band{left:0;top:3230px;width:1200px;height:457px}
.field-label{font-size:10px;font-weight:600;color:var(--white);left:461px}
.input{left:461px;width:277px;height:25px;background:var(--white);border:1px solid #d8d8d8;font-size:10px;color:#8a8a8a;padding:6px 10px}
</style>
</head>
<body>

<header class="abs site-header">
  <div class="abs brand">ResonanzRaum</div>
  <nav class="abs nav"><span class="active">Start</span><span>Julius Brandt</span><span>ResonanzRaum</span><span>Termine</span><span>Blog</span><span>Kontakt</span></nav>
</header>

<section class="abs hero" role="img" aria-label="Heller Himmel mit Wolken und warmem Sonnenlicht"></section>
<svg class="abs hero-curve" viewBox="0 0 1200 80" preserveAspectRatio="none"><path d="M0 14 Q600 -18 1200 46 L1200 80 L0 80 Z" fill="#fffdf6"/></svg>
<div class="abs hero-title" style="top:190px;font-size:50px;letter-spacing:2px">willkommen</div>
<div class="abs hero-title" style="top:244px;font-size:18px">im</div>
<svg class="abs" style="left:452px;top:256px" width="296" height="2"><rect x="0" width="130" height="1" fill="#fff"/><rect x="166" width="130" height="1" fill="#fff"/></svg>
<div class="abs hero-title" style="top:258px;font-size:52px;font-weight:600;letter-spacing:2px">ResonanzRaum</div>
<div class="btn" style="left:565px;top:333px;width:70px">Tritt Ein!</div>

<svg class="abs" style="left:580px;top:508px" width="40" height="40"><circle cx="20" cy="20" r="19" fill="#45afd3"/><path d="M20 12v15M15 22l5 5 5-5" stroke="#fff" stroke-width="1.5" fill="none"/></svg>

<div class="abs tabs"><span class="on">wach werden</span><span>lebending sein</span><span>frei leben</span></div>
<div class="abs rule" style="left:223px;top:637px;width:754px"></div>

<div class="abs" style="left:540px;top:695px;width:120px;height:120px;border-radius:50%;border:2px solid var(--rule);background:radial-gradient(circle,#d3a987 0%,#a9b89a 70%,#e8e8e8 100%)" role="img" aria-label="Porträtfoto von Julius Brandt"></div>
<div class="abs serif center" style="left:0;width:1200px;top:825px;font-size:32px;font-weight:600;color:var(--ink)">Julius Brandt</div>
<div class="abs short-rule" style="top:873px"></div>
<p class="abs para" style="left:285px;width:630px;top:895px">Es ist mir eine tiefe Herzensangelegenheit, die Menschen, welche in einem erweiterten Bewusstsein leben möchten, in den ResonanzRaum initial hineinzuführen, damit sie sich erinnern und all die Weisheit, Freiheit und Liebe wieder ganz bei sich wachrufen und integrieren können.</p>
<p class="abs para" style="left:285px;width:630px;top:959px">Um dieser tiefgreifenden und lebensverändernden Arbeit gerecht zu werden, steht stetiges Lernen, Loslassen und Entwickeln für mich an erster Stelle. Ich begebe mich regelmäßig sowohl aktiv als auch unwillkürlich in tiefe Reinigungsprozesse und erlebe für mich, dass dieses eigene konsequente Vorangehen die unabdingbare Basis dafür ist, um andere Menschen erfolgreich begleiten zu können.</p>
<div class="btn" style="left:489px;top:1045px;width:222px">mehr über Julius Brandt erfahren <svg viewBox="0 0 14 10"><path d="M0 5h12M8 1l4 4-4 4" stroke="#fff" fill="none" stroke-width="1.3"/></svg></div>
<div class="abs rule" style="left:223px;top:1110px;width:754px"></div>

<div class="ph video" style="left:223px;top:1147px" role="img" aria-label="Videovorschau: Julius Brandt vor einem Bücherregal"><span class="play"></span></div>
<div class="ph video" style="left:481px;top:1147px" role="img" aria-label="Videovorschau: Julius Brandt vor einem Bücherregal"><span class="play"></span></div>
<div class="ph video" style="left:738px;top:1147px" role="img" aria-label="Videovorschau: Julius Brandt vor einem Bücherregal"><span class="play"></span></div>
<div class="ph video" style="left:352px;top:1313px" role="img" aria-label="Videovorschau: Julius Brandt vor einem Bücherregal"><span class="play"></span></div>
<div class="ph video" style="left:610px;top:1313px" role="img" aria-label="Videovorschau: Julius Brandt vor einem Bücherregal"><span class="play"></span></div>
<div class="btn" style="left:478px;top:1480px;width:244px"><svg viewBox="0 0 14 10" style="width:13px"><rect width="14" height="10" rx="2" fill="#fff"/></svg>zum Videokanal von Julius Brandt</div>

<div class="abs serif center" style="left:0;width:1200px;top:1582px;font-size:32px;font-weight:600;color:var(--ink);line-height:36px">Lesen im ResonanzRaum,<br>was bringt mir das?</div>
<div class="abs short-rule" style="top:1667px"></div>
<div class="abs feat" style="left:232px"><h3>Schwingungserhöhung<br>&nbsp;</h3><p>Deine körperliche und geistige Frequenz wird angehoben. Dies ermöglicht dir wieder wahrhaft fühlen zu können, eine erweiterte geistige Wahrnehmung und die Möglichkeit, deine eigenen höheren Energien und Potenziale zu öffnen und zu nutzen.</p></div>
<div class="abs feat" style="left:490px"><h3>Keine weitere Methode,<br>die du lernst</h3><p>Es ist die Öffnung deines geistigen Sinns, der dir Informationen jenseits deiner 5 irdischen Sinne bietet. Dies ist dein Zugang zu unbegrenzten Möglichkeiten und wenn du so willst, zu einer unbegrenzten Anzahl von neuen Methoden.</p></div>
<div class="abs feat" style="left:747px"><h3>Inspiration und<br>Kreativität</h3><p>Die Schwingung des ResonanzRaums ist jenseits des menschlichen Verstandes – verbindest du dich damit, intensivierst du den Zugang zu deiner Intuition. Dies beschert dir ausgeprägtere Inspirationen und ermöglicht dir eine höhere Kreativität.</p></div>

<div class="abs band"></div>
<div class="card" style="left:223px;top:1919px;height:344px"><div class="img" style="background:linear-gradient(180deg,#dfe4e6,#b8a590)" role="img" aria-label="Gruppe von Menschen mit erhobenen Armen"></div><h4>BasisWorkshop</h4><p>Im BasisWorkshop erlernst du den Zugang zum ResonanzRaum und wie du für dich und andere darin lesen und arbeiten kannst. Anhand unterschiedlicher Übungen erlangst du Sicherheit im Umgang mit dem Raum.</p><div class="btn">Termine <svg viewBox="0 0 14 10"><path d="M0 5h12M8 1l4 4-4 4" stroke="#fff" fill="none" stroke-width="1.3"/></svg></div></div>
<div class="card" style="left:481px;top:1919px;height:344px"><div class="img" style="background:linear-gradient(180deg,#f6d9a0,#d99a4f 70%,#8b6a45)" role="img" aria-label="Frau mit ausgebreiteten Armen im Sonnenuntergang"></div><h4>AufbauWorksops</h4><p>Um spezifische Themen und Entwicklungsbereiche noch intensiver und gezielter bearbeiten zu können, wurden die AufbauWorkshops entwickelt. Voraussetzung für die Teilnahme ist ein absolvierter BasisWorkshop.</p><div class="btn">Termine <svg viewBox="0 0 14 10"><path d="M0 5h12M8 1l4 4-4 4" stroke="#fff" fill="none" stroke-width="1.3"/></svg></div></div>
<div class="card" style="left:738px;top:1919px;height:344px"><div class="img" style="background:linear-gradient(180deg,#cfe4ee,#a7c3cf 70%,#8a7663)" role="img" aria-label="Zwei Wanderer helfen sich auf einem Felsen"></div><h4>Einzelsitzungen</h4><p>Wenn du Themen oder Aufgaben in deinem Leben hast, bei denen du nicht weiterkommst, dann treten wir in den ResonanzRaum ein und rufen dort die notwendigen Informationen und Handlungshinweise für dich ab.</p><div class="btn">Termine <svg viewBox="0 0 14 10"><path d="M0 5h12M8 1l4 4-4 4" stroke="#fff" fill="none" stroke-width="1.3"/></svg></div></div>

<div class="abs serif center" style="left:0;width:1200px;top:2332px;font-size:32px;color:var(--ink)">Anwendungsgebiete</div>
<p class="abs para" style="left:300px;width:600px;top:2392px;line-height:15px">Die <b>Anwendungsgebiete</b> sind nahezu <b>unerschöpflich</b>. Da der ResonanzRaum mit allen Informationen verbunden ist, können Fragen aus vielfältigen Themengebieten beantwortet werden. Einschränkungen bestehen jedoch hinsichtlich konkreter Voraussagen für die Zukunft. Zum einen können unterschiedliche Entscheidungen die Zukunft verändern, zum anderen ist es nicht die Aufgabe des ResonanzRaums dir wichtige Erfahrungen bereits im Vorfeld preiszugeben.</p>
<div class="btn" style="left:538px;top:2489px;width:124px">Mehr erfahren <svg viewBox="0 0 14 10"><path d="M0 5h12M8 1l4 4-4 4" stroke="#fff" fill="none" stroke-width="1.3"/></svg></div>

<div class="card" style="left:339px;top:2589px;height:318px"><div class="img" style="background:linear-gradient(180deg,#e9b45c,#a7763a 60%,#4b4a2a)" role="img" aria-label="Person auf einem Waldweg im Gegenlicht"></div><h4>OnlineErlebnisAbend Der ResonanzRaum</h4><p>Einführungsseminar und dafür gedacht, dich in einen intensiven ersten Kontakt mit dem ResonanzRaum zu bringen.</p><div class="btn">Termine <svg viewBox="0 0 14 10"><path d="M0 5h12M8 1l4 4-4 4" stroke="#fff" fill="none" stroke-width="1.3"/></svg></div></div>
<div class="card" style="left:610px;top:2589px;height:318px"><div class="img" style="background:linear-gradient(180deg,#f5e0b0,#e5b964 60%,#c59a4c)" role="img" aria-label="Meditierende Frau auf einem Feld bei Sonnenuntergang"></div><h4>LiveMeditationen</h4><p>Hier findest du von Julius Brandt geführte Live-Online-Meditationen im ResonanzRaum zu unterschiedlichen Themen.</p><div class="btn">Termine <svg viewBox="0 0 14 10"><path d="M0 5h12M8 1l4 4-4 4" stroke="#fff" fill="none" stroke-width="1.3"/></svg></div></div>

<div class="abs serif center" style="left:0;width:1200px;top:2950px;font-size:110px;line-height:110px;color:var(--blue);font-weight:700">”</div>
<p class="abs para" style="left:290px;width:620px;top:3048px;font-style:italic;font-size:11px;line-height:15px">Die Bereicherung, die dieser Kurs bietet, ist kaum in Worte zu fassen. Durch eine einfache und unkomplizierte Weise erfährt man, wie man intensiver mit seinem eigenen Selbst in Kontakt kommt. Für Fragen und Hilfestellungen stehen einem immer liebe Helfer zur Seite. Der Kurs ist wirklich für alle geeignet, selbst für die, die sich mit dem Thema „erweitertes Bewusstsein“ noch nicht beschäftigt haben. Ich kann es nur jedem ans Herz legen, selber diese Erfahrung zu machen.</p>
<p class="abs para" style="left:0;width:1200px;top:3143px;font-size:11px"><b>Marta Keller</b>, Bereichsleitung Marketing</p>
<svg class="abs" style="left:578px;top:3177px" width="44" height="8"><circle cx="5" cy="4" r="3.5" fill="#45afd3"/><circle cx="22" cy="4" r="3.5" fill="#9a9a9a"/><circle cx="39" cy="4" r="3.5" fill="#9a9a9a"/></svg>

<svg class="abs footer-band" viewBox="0 0 1200 457" preserveAspectRatio="none"><path d="M0 34 Q600 -20 1200 26 L1200 457 L0 457 Z" fill="#45afd3"/></svg>
<div class="abs serif center" style="left:0;width:1200px;top:3272px;font-size:30px;font-weight:600;color:var(--white)">Newsletter</div>
<div class="abs field-label" style="top:3342px">E-Mail Adresse (erforderlich)</div>
<div class="abs input" style="top:3362px">E-Mail</div>
<div class="abs field-label" style="top:3408px">Bitte Vornamen eingeben</div>
<div class="abs input" style="top:3428px">Vornamen</div>
<div class="abs field-label" style="top:3474px">Bitte Nachname eingeben</div>
<div class="abs input" style="top:3494px">Nachname</div>
<svg class="abs" style="left:461px;top:3552px" width="10" height="10"><rect width="10" height="10" fill="#fff"/><path d="M2 5l2 2 4-4" stroke="#45afd3" stroke-width="1.5" fill="none"/></svg>
<p class="abs" style="left:481px;top:3550px;width:260px;font-size:8.5px;line-height:13px;color:var(--white)">Ich habe die Datenschutzerklärung gelesen und stimme der elektronischen Übermittlung zu.</p>
<div class="btn" style="left:461px;top:3589px;width:277px;background:var(--white);color:var(--blue)">Anmelden <svg viewBox="0 0 14 10"><path d="M0 5h12M8 1l4 4-4 4" stroke="#45afd3" fill="none" stroke-width="1.3"/></svg></div>
<div class="abs" style="left:205px;top:3650px;width:790px;height:1px;background:rgba(255,255,255,.6)"></div>
<div class="abs" style="left:205px;top:3663px;font-size:8.5px;color:var(--white)">© 2021 Julius Brandt</div>
<div class="abs" style="right:205px;top:3663px;font-size:8.5px;color:var(--white)">Impressum | Datenschutz | AGB | Kontakt</div>

</body>
</html>
```